Gutter Cleaning, Power Washing and exterior window washing

I need a flyer made for my business I am starting.
I will be doing gutter cleaning, power washing (Concrete driveways, sidewalks, porches, ect.) and exterior window washing.

I would like the flyer to be on one page. I want the back to be black.

I would like the services I offer to be in bullet points in this order:

Gutter cleaning
Power Washing (Concrete surfaces)
Exterior window washing

I would like the flyer to not be super 'busy' and distracting. A good simple design thats not too boring but again, not too busy.

I would like the colors to be a mix of:

Black
Turquoise

Somewhere on the flyer I would like it to say something like "Call or text Morgan Pellicott to schedule...." you can make something up but it needs to say something like that on there.

I don't want generic pictures of power washing or window cleaning or gutter cleaning, please.

Target Market(s)

Residential Customers

Industry/Entity Type

Business

Font styles to use
Sans Serif

Colors
000000
0592cd

Requirements
Must have
• Gutter cleaning
• Power Washing (Concrete surfaces)
• Exterior window washing
• all in bullet points in this order
Nice to have
• Cool modern design
Should not have
• Generic pictures

```html
<!DOCTYPE html>
<html lang="en">
<head>
<meta charset="utf-8">
<title>Exterior Cleaning Flyer – Front and Back</title>
<link href="https://fonts.googleapis.com/css2?family=Anton&family=Lato:wght@300;400;700&family=Roboto+Condensed:wght@300;400&display=swap" rel="stylesheet">
<style>
  :root {
    --teal: #00b5c4;
    --teal-deep: #0097a6;
    --black: #0a0a0a;
    --ink: #151515;
    --white: #ffffff;
    --rule: #c9c9c9;
    --backdrop: #b4b4b4;
    --photo-blue: #3f5c86;
    --photo-warm: #b8a69a;
    --photo-city: #8a98a6;
    --photo-green: #5f8a4a;
  }
  * { margin: 0; padding: 0; box-sizing: border-box; }
  html, body { width: 1200px; height: 1200px; overflow: hidden; }
  body { background: var(--backdrop); font-family: "Lato", sans-serif; position: relative; }

  .sheet {
    position: absolute; top: 290px; width: 513.6px; height: 720px; overflow: hidden;
    box-shadow: 0 6px 14px rgba(0,0,0,.25);
  }
  .sheet--front { left: 61px; background: var(--white); }
  .sheet--back { left: 639px; background: var(--black); }
  .sheet__inner {
    position: absolute; left: 0; top: 0; width: 642px; height: 900px;
    transform: scale(0.8); transform-origin: 0 0;
  }
  .sheet__art { position: absolute; inset: 0; width: 642px; height: 900px; }

  .abs { position: absolute; white-space: nowrap; }

  /* Front */
  .headline-light { left: 22px; top: 490px; font-family: "Roboto Condensed", sans-serif; font-weight: 300; font-size: 58px; color: var(--ink); line-height: 1; }
  .headline-bold { left: 22px; top: 553px; font-family: "Anton", sans-serif; font-size: 40px; color: var(--teal); letter-spacing: 1px; line-height: 1; }
  .tagline { left: 22px; top: 605px; width: 522px; height: 38px; background: var(--black);
    clip-path: polygon(0 0, 100% 0, 94% 100%, 0 100%); color: var(--white); font-size: 21px; line-height: 38px; padding-left: 9px; font-weight: 700; }
  .tagline span { font-weight: 300; text-transform: uppercase; }

  .services { left: 0; top: 660px; width: 642px; list-style: none; }
  .service { position: absolute; width: 200px; text-align: center; font-size: 19px; color: var(--ink); line-height: 23px; }
  .service__icon { display: block; margin: 0 auto 10px; width: 56px; height: 56px; border-radius: 6px; background: var(--teal); opacity: .9; }
  .service--gutter { left: 2px; top: 0; }
  .service--wash { left: 203px; top: 0; }
  .service--window { left: 404px; top: -3px; }
  .service--window .service__icon { height: 54px; }

  .contact { display: flex; align-items: center; }
  .contact__badge { width: 26px; height: 26px; }
  .contact__label { margin-left: 8px; line-height: 1.05; }
  .contact__label b { display: block; font-size: 16.5px; font-weight: 700; }
  .contact__label small { display: block; font-family: "Roboto Condensed", sans-serif; font-size: 13.5px; }
  .contact__number { margin-left: 14px; font-family: "Roboto Condensed", sans-serif; font-size: 40px; color: var(--teal); letter-spacing: .5px; }
  .contact--front { left: 146px; top: 798px; color: var(--ink); }
  .contact--back { left: 150px; top: 745px; color: var(--white); }

  .rule { position: absolute; height: 2px; }
  .rule--front { left: 92px; top: 850px; width: 458px; background: var(--rule); }
  .rule--back { left: 96px; top: 815px; width: 458px; background: var(--white); }

  .footer-item { display: flex; align-items: center; font-size: 11.5px; }
  .footer-item svg { width: 12px; height: 12px; margin-right: 9px; }
  .front-foot { color: #333; top: 864px; }
  .back-foot { color: var(--white); top: 838px; }

  /* Back */
  .call-line { left: 74px; top: 370px; font-family: "Anton", sans-serif; font-size: 52px; color: var(--teal); letter-spacing: 1px; line-height: 1; }
  .caller { left: 72px; top: 438px; font-size: 60px; color: var(--white); line-height: 1; }
  .schedule { left: 74px; top: 527px; width: 504px; height: 89px; background: var(--teal);
    font-family: "Roboto Condensed", sans-serif; font-size: 92px; line-height: 90px; color: var(--black); padding-left: 6px; letter-spacing: -1px; }
  .blurb { position: absolute; left: 32px; top: 650px; width: 590px; font-size: 14.4px; line-height: 18px; color: var(--white); text-align: justify; }
</style>
</head>
<body>

<section class="sheet sheet--front" aria-label="Flyer front">
  <div class="sheet__inner">
    <svg class="sheet__art" viewBox="0 0 642 900" aria-hidden="false">
      <defs>
        <linearGradient id="mist" x1="0" y1="0" x2="1" y2="1">
          <stop offset="0" stop-color="#f3f3f3"/><stop offset=".5" stop-color="#ffffff"/><stop offset="1" stop-color="#eeeeee"/>
        </linearGradient>
        <linearGradient id="handshakePhoto" x1="0" y1="0" x2="1" y2="1">
          <stop offset="0" stop-color="#9a9a94"/><stop offset=".45" stop-color="var(--photo-blue)"/><stop offset="1" stop-color="var(--photo-warm)"/>
        </linearGradient>
        <linearGradient id="cityPhoto" x1="0" y1="0" x2="1" y2="1">
          <stop offset="0" stop-color="var(--photo-city)"/><stop offset=".6" stop-color="#c9c3b8"/><stop offset="1" stop-color="#e8d6b8"/>
        </linearGradient>
        <linearGradient id="gardenPhoto" x1="0" y1="0" x2="1" y2="1">
          <stop offset="0" stop-color="var(--photo-green)"/><stop offset=".6" stop-color="#9aa59a"/><stop offset="1" stop-color="#cfd3cf"/>
        </linearGradient>
      </defs>
      <rect width="642" height="900" fill="url(#mist)"/>
      <polygon points="188,0 642,0 642,300 418,502 55,130" fill="var(--black)"/>
      <polygon points="212,0 642,0 642,288 414,486 74,136" fill="url(#handshakePhoto)" role="img" aria-label="Photo of a smiling technician shaking hands with a homeowner"/>
      <polygon points="642,290 642,400 582,352" fill="var(--teal)"/>
      <polygon points="589,338 642,388 642,590 575,655 437,516" fill="var(--black)"/>
      <polygon points="589,358 642,408 642,572 575,632 458,516" fill="url(#gardenPhoto)" role="img" aria-label="Photo of a clean stone garden path with plants"/>
      <polygon points="241,218 394,368 241,518 88,368" fill="var(--white)"/>
      <polygon points="241,238 374,368 241,498 108,368" fill="url(#cityPhoto)" role="img" aria-label="Photo of sparkling high-rise windows at sunset"/>
      <polygon points="241,226 386,368 241,510 96,368" fill="none" stroke="var(--teal)" stroke-width="6"/>
    </svg>

    <div class="abs headline-light">NOBODY</div>
    <div class="abs headline-bold">DOES IT BETTER</div>
    <div class="abs tagline">Where <span>Spotless Cleaning</span> comes to your door</div>

    <ul class="abs services">
      <li class="service service--gutter"><span class="service__icon" role="img" aria-label="Gutter cleaning icon"></span>Gutter cleaning</li>
      <li class="service service--wash"><span class="service__icon" role="img" aria-label="Power washing icon"></span>Power Washing<br>(Concrete surfaces)</li>
      <li class="service service--window"><span class="service__icon" role="img" aria-label="Window washing icon"></span>Exterior window<br>washing</li>
    </ul>

    <div class="abs contact contact--front">
      <svg class="contact__badge" viewBox="0 0 26 26"><circle cx="13" cy="13" r="13" fill="var(--teal)"/><path d="M9 7c1 0 2 2 2 3s-1 1-1 2c0 1 2 3 3 3 1 0 1-1 2-1s3 1 3 2-1 3-3 3c-4 0-9-5-9-9 0-2 2-3 3-3z" fill="var(--white)"/></svg>
      <div class="contact__label"><b>Contact us</b><small>For More Information</small></div>
      <div class="contact__number">0000000000</div>
    </div>
    <div class="rule rule--front"></div>

    <div class="abs footer-item front-foot" style="left:30px"><svg viewBox="0 0 12 12"><circle cx="6" cy="6" r="5" fill="var(--teal)"/></svg>your web address goes here</div>
    <div class="abs footer-item front-foot" style="left:236px"><svg viewBox="0 0 12 12"><rect x="1" y="3" width="10" height="7" fill="var(--teal)"/></svg>your email address goes here</div>
    <div class="abs footer-item front-foot" style="left:460px"><svg viewBox="0 0 12 12"><path d="M6 0a4 4 0 0 1 4 4c0 3-4 8-4 8S2 7 2 4a4 4 0 0 1 4-4z" fill="var(--teal)"/></svg>your address goes here</div>
  </div>
</section>

<section class="sheet sheet--back" aria-label="Flyer back">
  <div class="sheet__inner">
    <svg class="sheet__art" viewBox="0 0 642 900">
      <defs>
        <linearGradient id="tealWash" x1="0" y1="0" x2="1" y2="1">
          <stop offset="0" stop-color="#00c3cf"/><stop offset="1" stop-color="var(--teal-deep)"/>
        </linearGradient>
        <radialGradient id="grunge" cx=".5" cy=".45" r=".6">
          <stop offset="0" stop-color="#222"/><stop offset="1" stop-color="var(--black)"/>
        </radialGradient>
      </defs>
      <rect width="642" height="900" fill="url(#grunge)"/>
      <polygon points="161,0 446,0 0,363 0,123" fill="url(#tealWash)"/>
      <polygon points="516,0 642,0 642,355 314,178" fill="url(#tealWash)"/>
    </svg>

    <div class="abs call-line">CALL OR TEXT</div>
    <div class="abs caller">Morgan Pellicott</div>
    <div class="abs schedule">TO SCHEDULE</div>
    <p class="blurb">Lorem Ipsum is simply dummy text of the printing and typesetting industry. Lorem Ipsum has been the industry's standard dummy text ever since the 1500s, when an unknown printer took a galley of type and scrambled it to make a type specimen book.</p>

    <div class="abs contact contact--back">
      <svg class="contact__badge" viewBox="0 0 26 26"><circle cx="13" cy="13" r="13" fill="var(--teal)"/><path d="M9 7c1 0 2 2 2 3s-1 1-1 2c0 1 2 3 3 3 1 0 1-1 2-1s3 1 3 2-1 3-3 3c-4 0-9-5-9-9 0-2 2-3 3-3z" fill="var(--white)"/></svg>
      <div class="contact__label"><b>Contact us</b><small>For More Information</small></div>
      <div class="contact__number">0000000000</div>
    </div>
    <div class="rule rule--back"></div>

    <div class="abs footer-item back-foot" style="left:34px"><svg viewBox="0 0 12 12"><circle cx="6" cy="6" r="5" fill="var(--teal)"/></svg>your web address goes here</div>
    <div class="abs footer-item back-foot" style="left:239px"><svg viewBox="0 0 12 12"><rect x="1" y="3" width="10" height="7" fill="var(--teal)"/></svg>your email address goes here</div>
    <div class="abs footer-item back-foot" style="left:466px"><svg viewBox="0 0 12 12"><path d="M6 0a4 4 0 0 1 4 4c0 3-4 8-4 8S2 7 2 4a4 4 0 0 1 4-4z" fill="var(--teal)"/></svg>your address goes here</div>
  </div>
</section>

</body>
</html>
```